Delvin & Associates - London New Letting and Property Management Company *

Delvin & Associates LTD is a new company based in London, and works with brand new residential property in the city centre.

We are aiming to have 1000 new properties a year.

We are looking for something modern and minimalistic :
Logo ,Monogram, Paper Head and Business Card.

Target Market(s)

Internation landlords

Industry/Entity Type

Real Estate

Logo Text

Delvin & Associates

Colors

Designer to choose colors to be used in the design.

Requirements
Nice to have
• A particular monogram with "DA"
Should not have
• Little House over the logo

```html
<!DOCTYPE html>
<html lang="en">
<head>
<meta charset="utf-8">
<title>Delvin &amp; Associates LTD – Stationery</title>
<link rel="stylesheet" href="https://fonts.googleapis.com/css2?family=Libre+Baskerville:wght@400;700&display=swap">
<style>
  :root {
    --backdrop: #f3f3f3;
    --paper: #ffffff;
    --ink: #1a1a1a;
    --brand-blue: #558cd0;
    --brand-green: #5db584;
    --name-blue: #7ba8e2;
    --card-ink: #1f3a2a;
  }
  * { margin: 0; padding: 0; box-sizing: border-box; }
  html, body {
    width: 1200px; height: 785px; overflow: hidden;
    background: var(--backdrop);
    font-family: "Libre Baskerville", Georgia, serif;
    color: var(--ink);
  }
  .stationery { position: relative; width: 1200px; height: 785px; }

  /* Letterhead */
  .letterhead {
    position: absolute; left: 110px; top: 45px;
    width: 490px; height: 694px;
    background: var(--paper);
    box-shadow: 0 2px 10px rgba(0,0,0,.08);
  }
  .wordmark {
    position: absolute; left: 0; right: 0; top: 70px;
    text-align: center;
  }
  .wordmark-square {
    display: block; width: 14px; height: 14px; margin: 0 auto 12px;
    background: var(--ink);
  }
  .wordmark-name {
    font-size: 11px; font-weight: 700; letter-spacing: .12em; text-transform: uppercase;
  }
  .tab { position: absolute; width: 16px; height: 6px; }
  .tab--blue { background: var(--brand-blue); }
  .tab--green { background: var(--brand-green); }
  .letterhead .tab-left  { left: 0; top: 185px; }
  .letterhead .tab-top   { right: 40px; top: 42px; }
  .letterhead .tab-right { right: 0; top: 520px; }

  .address {
    position: absolute; right: 40px; top: 470px;
    text-align: right; font-size: 9px; font-weight: 700; line-height: 1.5;
  }
  .contact {
    position: absolute; left: 40px; bottom: 40px;
    font-size: 9px; font-weight: 700; line-height: 1.5;
  }

  /* Business cards */
  .card {
    position: absolute; width: 320px; height: 198px;
    box-shadow: 0 2px 10px rgba(0,0,0,.1);
  }
  .card--front {
    left: 660px; top: 500px;
    background: var(--brand-blue);
    display: flex; flex-direction: column; align-items: center; justify-content: center;
  }
  .card--front .wordmark-square { width: 12px; height: 12px; margin-bottom: 10px; }
  .card--front .wordmark-name { font-size: 10px; }

  .card--back {
    left: 830px; top: 230px;
    background: var(--brand-green);
    color: var(--card-ink);
  }
  .card-person { position: absolute; left: 30px; top: 34px; }
  .card-name {
    font-size: 30px; font-weight: 400; line-height: 1.05;
    color: var(--name-blue);
  }
  .card-role { margin-top: 8px; font-size: 8px; font-weight: 700; }
  .card--back .address { top: 30px; right: 22px; font-size: 7px; }
  .card--back .contact { left: 30px; bottom: 24px; font-size: 7px; }
  .card--back .tab { right: 0; top: 96px; width: 12px; height: 5px; }
</style>
</head>
<body>
<main class="stationery">

  <section class="letterhead" aria-label="Letterhead">
    <span class="tab tab--blue tab-left"></span>
    <span class="tab tab--green tab-top"></span>
    <header class="wordmark">
      <span class="wordmark-square"></span>
      <p class="wordmark-name">Delvin &amp; Associates LTD</p>
    </header>
    <address class="address" style="font-style:normal">
      2140 Elm Terrace<br>LONDON<br>W1X 7QB
    </address>
    <span class="tab tab--blue tab-right"></span>
    <p class="contact">
      +44 7700 900 418<br>
      hello@delvinoffice.co.uk<br>
      www.delvinassociates.co.uk
    </p>
  </section>

  <section class="card card--back" aria-label="Business card, back">
    <div class="card-person">
      <p class="card-name">Owen<br>Hale</p>
      <p class="card-role">Real Estate Agent</p>
    </div>
    <address class="address" style="font-style:normal">
      2140 Elm Terrace<br>LONDON<br>W1X 7QB
    </address>
    <span class="tab tab--blue"></span>
    <p class="contact">
      +44 7700 900 418<br>
      hello@delvinoffice.co.uk<br>
      www.delvinassociates.co.uk
    </p>
  </section>

  <section class="card card--front" aria-label="Business card, front">
    <span class="wordmark-square"></span>
    <p class="wordmark-name">Delvin &amp; Associates LTD</p>
  </section>

</main>
</body>
</html>
```